Farm product labels

This is meant to design a set of labels for the following products:
Sachets (similar to Brannigan’s ketchup):
- Size: W4xH9 cm. This is the internal area (inside the four sealing borders) of sachets. Front side contains the design, and back side just texts with the ingredients, nutrition facts and origin. Please check check the attached pictures related to sachet designs for your reference!
- Products:
o Ketchup
o Honey
o Nubakora (chocolate spread made of cacao, peanuts, and milk)
o Peanut butter
o Fruit jam (either Mango, Guava or Passion fruit)

Stickers (to be added on transparent bags):
- Size: W8xH14 cm. It does not need to be rectangular
- It needs to accommodate small texts with the ingredients, nutrition facts and origin
- Products:
o Tomato paste
o Fruit pulp (either Mango, Guava or Passion fruit)
o Processed vegetables (either Yuca or Sweet potato). They are peeled, chopped, pre-boiled and frozen.

For those interested I’ll provide detailed info as required

Target Market(s)

Hotels. The sachets are specially for breakfast

Requirements
Must have
• All product label designs should:
- Show a similar look, reflecting a single source/branding
- Be attractive and be easy to recognize each product
- Contain the logo of our farm (uploaded)

```html
<!DOCTYPE html>
<html lang="en">
<head>
<meta charset="utf-8">
<title>Finca Las Brisas – Sachet Labels</title>
<link rel="stylesheet" href="https://fonts.googleapis.com/css2?family=Oswald:wght@300;400&display=swap">
<style>
  :root {
    --bg: #ffffff;
    --face-light: #fbfbfb;
    --face-shade: #e9e9e9;
    --seal-light: #f4f4f4;
    --seal-dark: #e3e3e3;
    --seal-edge: #d2d2d2;
    --brand-blue: #2a4a9a;
    --ketchup-red: #d23b35;
    --pulp-rose: #b34a63;
    --ink: #222222;
    --leaf-light: #c9dcaa;
    --leaf: #6e9b45;
    --leaf-dark: #3f6b2a;
    --tomato: #d9532e;
    --passion: #7a2c3e;
  }
  * { margin: 0; padding: 0; box-sizing: border-box; }
  html, body {
    width: 1200px; height: 1200px; overflow: hidden;
    background: var(--bg);
    font-family: "Oswald", "Arial Narrow", sans-serif;
  }
  .canvas { position: relative; width: 1200px; height: 1200px; }

  .sachet {
    position: absolute; left: 147px; width: 930px; height: 435px;
  }
  .sachet--ketchup { top: 96px; }
  .sachet--pulp { top: 647px; }

  .sachet__shell {
    position: absolute; inset: 0; width: 100%; height: 100%;
    filter: drop-shadow(0 3px 5px rgba(0,0,0,0.12));
  }

  .sachet__face {
    position: absolute; top: 37px; bottom: 31px; left: 60px; right: 24px;
    border-radius: 14px;
    background: radial-gradient(ellipse at 40% 45%, var(--face-light) 55%, var(--face-shade) 100%);
    box-shadow:
      inset 0 0 22px rgba(0,0,0,0.10),
      inset 0 6px 10px rgba(255,255,255,0.8),
      0 0 0 1px rgba(0,0,0,0.03);
    overflow: hidden;
  }

  .brand {
    position: absolute; top: 50%;
    transform: translateY(-50%);
    display: flex; flex-direction: column; align-items: center; gap: 10px;
  }
  .sachet--ketchup .brand { left: 104px; }
  .sachet--pulp .brand { left: 66px; }
  .brand__dot {
    width: 24px; height: 24px; border-radius: 50%;
    background: var(--brand-blue);
  }
  .brand__name {
    writing-mode: vertical-rl; transform: rotate(180deg);
    font-weight: 400; font-size: 22px; letter-spacing: 2px;
    color: var(--brand-blue);
  }

  .product {
    position: absolute; top: 50%;
    writing-mode: vertical-rl;
    transform: translateY(-50%) rotate(180deg);
    white-space: nowrap;
  }
  .product__name {
    font-weight: 300; font-size: 66px; line-height: 1;
  }
  .sachet--ketchup .product__name { left: 237px; color: var(--ketchup-red); letter-spacing: 11px; }
  .sachet--pulp .product__name { left: 197px; color: var(--pulp-rose); letter-spacing: 5px; }

  .product__tagline {
    font-weight: 300; font-size: 25px; line-height: 1.5;
  }
  .sachet--ketchup .product__tagline { left: 322px; color: var(--brand-blue); }
  .sachet--pulp .product__tagline { left: 270px; color: var(--ink); text-align: center; }

  .artwork {
    position: absolute; top: 0; bottom: 0; right: 0;
    -webkit-mask-image: linear-gradient(to right, transparent 0%, #000 22%, #000 94%, transparent 100%);
    mask-image: linear-gradient(to right, transparent 0%, #000 22%, #000 94%, transparent 100%);
  }
  .artwork--tomatoes {
    width: 446px;
    background:
      radial-gradient(circle at 52% 30%, var(--tomato) 0 6%, transparent 14%),
      radial-gradient(ellipse at 55% 45%, var(--leaf) 0%, var(--leaf-dark) 45%, var(--leaf-light) 85%);
  }
  .artwork--passionfruit {
    width: 480px;
    background:
      radial-gradient(circle at 60% 68%, var(--passion) 0 14%, transparent 22%),
      radial-gradient(ellipse at 55% 50%, var(--leaf) 0%, var(--leaf-light) 75%, var(--face-light) 100%);
  }
</style>
</head>
<body>
<main class="canvas">

  <svg width="0" height="0" style="position:absolute" aria-hidden="true">
    <defs>
      <linearGradient id="seal-fill" x1="0" y1="0" x2="0" y2="1">
        <stop offset="0" stop-color="#f6f6f6"/>
        <stop offset="0.5" stop-color="#efefef"/>
        <stop offset="1" stop-color="#e2e2e2"/>
      </linearGradient>
    </defs>
  </svg>

  <section class="sachet sachet--ketchup">
    <svg class="sachet__shell" viewBox="0 0 930 435" aria-hidden="true">
      <path d="M4,0 H926 Q930,0 930,4 V8 L921,14 L930,20 V403 L921,409 L930,415 V431 Q930,435 926,435 H4 Q0,435 0,431 V415 L9,409 L0,403 V20 L9,14 L0,8 V4 Q0,0 4,0 Z"
            fill="url(#seal-fill)" stroke="#d2d2d2" stroke-width="1"/>
    </svg>
    <div class="sachet__face">
      <div class="brand">
        <span class="brand__dot"></span>
        <span class="brand__name">FINCA LAS BRISAS</span>
      </div>
      <h1 class="product product__name">KETCHUP</h1>
      <p class="product product__tagline">My Favourite One</p>
      <div class="artwork artwork--tomatoes" role="img" aria-label="Watercolour illustration of ripe tomatoes on a leafy vine"></div>
    </div>
  </section>

  <section class="sachet sachet--pulp">
    <svg class="sachet__shell" viewBox="0 0 930 435" aria-hidden="true">
      <path d="M4,0 H926 Q930,0 930,4 V8 L921,14 L930,20 V403 L921,409 L930,415 V431 Q930,435 926,435 H4 Q0,435 0,431 V415 L9,409 L0,403 V20 L9,14 L0,8 V4 Q0,0 4,0 Z"
            fill="url(#seal-fill)" stroke="#d2d2d2" stroke-width="1"/>
    </svg>
    <div class="sachet__face">
      <div class="brand">
        <span class="brand__dot"></span>
        <span class="brand__name">FINCA LAS BRISAS</span>
      </div>
      <h1 class="product product__name">FRUIT PULP</h1>
      <p class="product product__tagline">My Favourite One<br>Passion fruit</p>
      <div class="artwork artwork--passionfruit" role="img" aria-label="Watercolour illustration of purple passion fruits among green leaves"></div>
    </div>
  </section>

</main>
</body>
</html>
```